Classic Minimalistic Business Card

Design a classic, minimalistic Business Card. Please find inspiration in the attached Classic Minimalistic examples. My information:
Name: Glen Whitacre
Company: Whitacre Capital
Logo: WC
Address: 1800 N Corliss Ave, Suite 420 | Alder Falls, WI 53190
Phone: 630-555-0172
Email: glenwhitacre@tvm.example
Slogan: Building Wealth with Steady Purpose

Feel free to leave out any of the information above except my name.

I have selected Double-sided, but I am also open to Single-sided

Target Market(s)

22-70. income greater than 150k/year

Industry/Entity Type

Finance

Contact Information for Business Card

See Project Description

Requirements
Must have
• Ivory or "antiqued" background similar to the reference pictures

```html
<!DOCTYPE html>
<html lang="en">
<head>
<meta charset="utf-8">
<title>Whitacre Capital – Business Card</title>
<link rel="stylesheet" href="https://fonts.googleapis.com/css2?family=Cormorant+SC:wght@500;600&family=Pinyon+Script&display=swap">
<style>
  :root {
    --backdrop: #989d99;
    --ivory: #e6d8c6;
    --ink: #1a1614;
    --brick: #a33a2a;
    --seal-faint: rgba(150, 130, 110, 0.28);
  }
  html, body {
    margin: 0;
    padding: 0;
    width: 1200px;
    height: 1000px;
    overflow: hidden;
    background: var(--backdrop);
  }
  .card {
    position: absolute;
    left: 267px;
    top: 310px;
    width: 665px;
    height: 382px;
    background: var(--ivory);
    overflow: hidden;
    font-family: "Cormorant SC", Georgia, serif;
    color: var(--ink);
  }
  .company-name {
    position: absolute;
    left: 46px;
    top: 46px;
    margin: 0;
    font-size: 17px;
    font-weight: 600;
    line-height: 1.15;
    letter-spacing: 1.5px;
    color: var(--brick);
  }
  .tagline {
    position: absolute;
    left: 155px;
    top: 61px;
    margin: 0;
    font-size: 18px;
    font-weight: 500;
    letter-spacing: 2.6px;
    white-space: nowrap;
  }
  .holder-name {
    position: absolute;
    left: 0;
    right: 0;
    top: 180px;
    margin: 0;
    text-align: center;
    font-family: "Pinyon Script", cursive;
    font-weight: 400;
    font-size: 56px;
    line-height: 1;
  }
  .contact {
    position: absolute;
    left: 46px;
    top: 302px;
    font-size: 15px;
    font-weight: 600;
    letter-spacing: 1.6px;
    line-height: 17px;
  }
  .contact .phone { color: var(--brick); display: block; }
  .contact .email { display: block; font-variant: all-small-caps; font-size: 17px; letter-spacing: 1.8px; }
  .address {
    position: absolute;
    left: 300px;
    width: 285px;
    top: 302px;
    margin: 0;
    text-align: center;
    font-style: normal;
    font-size: 14px;
    font-weight: 600;
    letter-spacing: 1.2px;
    line-height: 17px;
  }
  .seal-decoration {
    position: absolute;
    left: 560px;
    top: 268px;
  }
</style>
</head>
<body>
  <div class="card">
    <p class="company-name">Whitacre<br>Capital</p>
    <p class="tagline">Building Wealth with Steady Purpose</p>
    <h1 class="holder-name">Glen Whitacre</h1>
    <div class="contact">
      <span class="phone">630-555-0172</span>
      <span class="email">glenwhitacre@tvm.example</span>
    </div>
    <address class="address">1800 N Corliss Ave,<br>Suite 420 | Alder Falls, WI 53190</address>
    <svg class="seal-decoration" width="110" height="110" viewBox="0 0 110 110" aria-hidden="true">
      <circle cx="55" cy="55" r="52" fill="none" stroke="var(--seal-faint)" stroke-width="2"/>
    </svg>
  </div>
</body>
</html>
```